Networking card

I just need a simple design with the following information:
Milan Dorsey
415.608.2931
mdorsey083651@quillpost.example

I would like to have a white background with blue text like in this sample: https://lumacardstudio.example/business-card-527306/

```html
<!DOCTYPE html>
<html lang="en">
<head>
<meta charset="utf-8">
<title>Milan Dorsey — Networking Card</title>
<link rel="stylesheet" href="https://fonts.googleapis.com/css2?family=Lexend+Exa:wght@700&family=Arimo:wght@400&display=swap">
<style>
  :root {
    --stage: #012034;
    --card: #ffffff;
    --navy: #0b3a5c;
    --ink: #2b2b2b;
    --gray: #bdbdbd;
    --art-light: #eef3f7;
    --art-mid: #d9e3ec;
  }
  * { margin: 0; padding: 0; box-sizing: border-box; }
  html, body {
    width: 1200px;
    height: 1000px;
    overflow: hidden;
    background: var(--stage);
  }
  .card {
    position: absolute;
    left: 75px;
    top: 200px;
    width: 1050px;
    height: 600px;
    background: var(--card);
    border-radius: 30px;
    overflow: hidden;
  }
  .card__name {
    position: absolute;
    left: 46px;
    top: 62px;
    font-family: "Lexend Exa", sans-serif;
    font-weight: 700;
    font-size: 44px;
    letter-spacing: 0.5px;
    color: var(--navy);
    text-transform: uppercase;
    line-height: 1;
  }
  .card__network {
    position: absolute;
    left: 488px;
    top: 165px;
    width: 512px;
    height: 255px;
    border-radius: 120px;
    background: radial-gradient(ellipse at center, var(--art-mid) 0%, var(--art-light) 55%, var(--card) 100%);
  }
  .contact {
    position: absolute;
    left: 47px;
    top: 424px;
    list-style: none;
  }
  .contact__item {
    display: flex;
    align-items: center;
    height: 36px;
    margin-bottom: 6px;
    font-family: "Arimo", sans-serif;
    font-size: 26px;
    color: var(--ink);
  }
  .contact__icon {
    width: 36px;
    height: 32px;
    margin-right: 11px;
    flex: none;
  }
  .card__bands {
    position: absolute;
    left: 0;
    top: 550px;
    width: 1050px;
    height: 18px;
  }
</style>
</head>
<body>
  <article class="card">
    <h1 class="card__name">Milan Dorsey</h1>

    <div class="card__network" role="img" aria-label="Illustration of a network of connected people icons in a hexagonal pattern"></div>

    <ul class="contact">
      <li class="contact__item">
        <svg class="contact__icon" viewBox="0 0 36 32" aria-hidden="true">
          <rect width="36" height="32" rx="4" fill="#0b3a5c"/>
          <rect x="12" y="6" width="12" height="20" rx="2" fill="none" stroke="#fff" stroke-width="2"/>
          <circle cx="18" cy="22.5" r="1.3" fill="#fff"/>
        </svg>
        <span>415.608.2931</span>
      </li>
      <li class="contact__item">
        <svg class="contact__icon" viewBox="0 0 36 32" aria-hidden="true">
          <rect width="36" height="32" rx="4" fill="#0b3a5c"/>
          <path d="M9 16 L27 8 L21 25 L17 18 Z" fill="#fff"/>
          <path d="M17 18 L27 8" stroke="#0b3a5c" stroke-width="1.5"/>
        </svg>
        <span>mdorsey083651@quillpost.example</span>
      </li>
    </ul>

    <svg class="card__bands" viewBox="0 0 1050 18" preserveAspectRatio="none" aria-hidden="true">
      <polygon points="0,0 538,0 520,18 0,18" fill="#0b3a5c"/>
      <polygon points="550,0 1050,0 1050,18 532,18" fill="#bdbdbd"/>
    </svg>
  </article>
</body>
</html>
```